Designing a brochures for an educational counseling service provider

We would like a 4 sided design on a 11x8.5 paper, half folded. I have including a sample design we did to give you an idea of what we envision but we welcome creativity to make beautiful looking flyers. Text for the flier is included as well as our logo.
- The most important thing is capturing our audience/market. We will be handing these flies to schools, organizations and individual clients.

www.plorvaeducationalconsultants.example

Target Market(s)

We are targeting international students wanting to study in the U.S and Canada.

Industry/Entity Type

Education

Requirements
Must have
• - Clean and clear
• - Our logo should visible and well placed.
• - Could you the pictures of students, libraries and school buildings or you could use the pictures we already have.
Nice to have
• We would like this to match business cards.

```html
<!DOCTYPE html>
<html lang="en">
<head>
<meta charset="utf-8">
<title>Plorva Educational Consultants – Brochure Cover</title>
<link href="https://fonts.googleapis.com/css2?family=Montserrat:wght@400;600;700&family=Roboto+Condensed:wght@500&display=swap" rel="stylesheet">
<style>
  :root{
    --navy:#1b3446;
    --slate:#3f5778;
    --orange:#f7862a;
    --orange-soft:#f9a04a;
    --gold:#f5b700;
    --green:#7cc243;
    --white:#ffffff;
    --ink:#1c1c1c;
    --page-bg:#a9a9a9;
  }
  *{box-sizing:border-box;margin:0;padding:0}
  html,body{width:948px;height:1200px;overflow:hidden;background:var(--page-bg)}
  body{font-family:"Montserrat",sans-serif;position:relative}
  .spread{position:absolute;left:24px;top:252px;width:900px;height:696px;background:var(--white);
    box-shadow:0 6px 18px rgba(0,0,0,.35);overflow:hidden}
  .panel{position:absolute;top:0;height:100%}
  .back{left:0;width:450px}
  .front{left:450px;width:450px}
  .topband{position:absolute;left:0;top:0;width:100%;height:180px;background:var(--navy)}
  .green-rule{position:absolute;left:0;top:180px;width:900px;height:5px;background:var(--green)}
  .kicker{position:absolute;left:28px;top:75px;font-weight:700;font-size:15.5px;color:var(--gold);letter-spacing:.2px}
  .subhead{position:absolute;left:28px;top:97px;font-weight:400;font-size:20px;color:var(--white);letter-spacing:.2px}
  .photo{position:absolute;top:185px;height:275px;width:450px}
  .photo-library{left:0;background:linear-gradient(135deg,#f4f1e4 0%,#e9d7c0 40%,#c8a58a 60%,#8d9bb0 100%)}
  .photo-students{left:0;background:linear-gradient(160deg,#d9c2a0 0%,#6b4a35 45%,#2a2a30 75%,#3d6fa8 100%)}
  .mission{position:absolute;left:0;top:460px;width:450px;height:59px;background:var(--orange-soft);
    color:var(--white);font-size:14.5px;text-align:center;line-height:19px;padding-top:10px}
  .contact-band{position:absolute;left:0;top:519px;width:450px;height:43px;background:var(--orange)}
  .contact-band h2{position:absolute;left:36px;top:11px;font-size:18px;font-weight:700;color:var(--white)}
  .contact{position:absolute;left:0;top:562px;width:450px;height:93px;background:var(--white)}
  .contact-list{position:absolute;left:16px;top:14px;list-style:none;font-size:10.5px;color:var(--ink)}
  .contact-list li{display:flex;align-items:flex-start;gap:8px;margin-bottom:5px}
  .contact-list svg{flex:none;margin-top:1px}
  .contact-list .phone{font-weight:700;font-size:13px}
  .contact-list .email{font-size:8.5px}
  .divider{position:absolute;left:218px;top:10px;width:1px;height:72px;background:var(--orange)}
  .role{position:absolute;left:244px;top:32px;font-size:8.5px;line-height:12px;color:var(--ink)}
  .footer{position:absolute;top:655px;height:41px;display:flex;align-items:center;justify-content:center;
    font-size:13.5px;font-weight:600;color:var(--white)}
  .footer-back{left:0;width:450px;background:var(--navy)}
  .footer-front{left:450px;width:450px;background:var(--orange)}
  .footer-arrow{position:absolute;left:450px;top:655px}
  .brand{position:absolute;left:60px;top:62px;display:flex;align-items:center;gap:14px}
  .brand-dot{width:56px;height:56px;border-radius:50%;background:var(--green)}
  .brand-name{font-weight:700;font-size:22px;line-height:26px;color:var(--white)}
  .tagline-band{position:absolute;left:0;top:460px;width:450px;height:102px;background:var(--slate)}
  .tagline{position:absolute;left:0;top:10px;width:100%;text-align:center;font-family:"Roboto Condensed",sans-serif;
    font-weight:500;font-size:19px;line-height:26px;color:var(--white)}
  .services{position:absolute;left:0;top:540px;width:450px;display:flex;justify-content:space-around;padding:0 14px;list-style:none}
  .service{width:100px;text-align:center;font-size:11px;font-weight:700;color:var(--navy);line-height:13px}
  .service .ring{width:62px;height:62px;margin:0 auto 8px;border-radius:50%;background:var(--white);
    border:3px solid var(--orange-soft);display:flex;align-items:center;justify-content:center}
</style>
</head>
<body>
<main class="spread">
  <div class="topband"></div>
  <div class="green-rule"></div>

  <section class="panel back">
    <p class="kicker">INTERNATIONAL EDUCATIONAL CONSULTANTS</p>
    <p class="subhead">INTERNATIONAL STUDENTS SOLUTIONS</p>
    <div class="photo photo-library" role="img" aria-label="Photo of a smiling student holding an open red book in a library"></div>
    <p class="mission">Our mission is to make quality educational accessible,<br>attainable and affordable to the families we serve.</p>
    <div class="contact-band"><h2>CONTACT US</h2></div>
    <div class="contact">
      <ul class="contact-list">
        <li><svg width="9" height="11" viewBox="0 0 9 11"><path d="M4.5 0a4 4 0 0 1 4 4c0 3-4 7-4 7S.5 7 .5 4a4 4 0 0 1 4-4z" fill="#f7862a"/><circle cx="4.5" cy="4" r="1.5" fill="#fff"/></svg>
          <span>418 Maple Crest Rd<br>Suite 12B, Linden, TX 75001</span></li>
        <li class="phone"><svg width="11" height="10" viewBox="0 0 11 10"><path d="M1 3c0-2 9-2 9 0v1H7.5V3h-4v1H1z M2 5h7l1 4H1z" fill="#f7862a"/></svg>
          <span>555-014-2290</span></li>
        <li class="email"><svg width="10" height="8" viewBox="0 0 10 8"><rect width="10" height="8" fill="#f7862a"/><path d="M0 0l5 4 5-4" stroke="#fff" fill="none"/></svg>
          <span>contact@plorvaeducationalconsultants.example</span></li>
      </ul>
      <div class="divider"></div>
      <p class="role">Executive Director &amp; Independent<br>Educational Consultant<br>Plorva International Educational Consultants, LLC</p>
    </div>
    <div class="footer footer-back">www.plorvaeducationalconsultants.example</div>
  </section>

  <section class="panel front">
    <div class="brand">
      <span class="brand-dot"></span>
      <span class="brand-name">PLORVA<br>International Educational<br>Consultants</span>
    </div>
    <div class="photo photo-students" role="img" aria-label="Photo of four smiling students studying together over open books"></div>
    <div class="tagline-band">
      <p class="tagline">A full-service international educational consulting group<br>serving students and families across the globe.</p>
    </div>
    <ul class="services">
      <li class="service"><div class="ring"><svg width="32" height="30" viewBox="0 0 32 30" fill="none" stroke="#555" stroke-width="1.5"><path d="M2 9L16 2l14 7z"/><path d="M4 11h24M6 13v11M11 13v11M16 13v11M21 13v11M26 13v11M3 26h26M2 28h28"/></svg></div>Boarding<br>Schools</li>
      <li class="service"><div class="ring"><svg width="30" height="30" viewBox="0 0 30 30" fill="none" stroke="#555" stroke-width="1.5"><path d="M6 3h13l5 5v19H6z"/><path d="M19 3v5h5"/><path d="M12 22l2-6 11-11 3 3-11 11z"/></svg></div>College<br>Admission</li>
      <li class="service"><div class="ring"><svg width="34" height="28" viewBox="0 0 34 28" fill="none" stroke="#555" stroke-width="1.5"><path d="M2 10L17 3l15 7-15 7z"/><path d="M8 13v7c3 3 15 3 18 0v-7"/><path d="M30 11v9"/></svg></div>Transfer<br>Students</li>
      <li class="service"><div class="ring"><svg width="34" height="28" viewBox="0 0 34 28" fill="none" stroke="#555" stroke-width="1.5"><circle cx="11" cy="7" r="4"/><path d="M3 20c0-5 4-7 8-7s8 2 8 7z"/><circle cx="24" cy="12" r="3.5"/><path d="M17 25c0-4 3-6 7-6s7 2 7 6z"/></svg></div>Graduate<br>Students</li>
    </ul>
  </section>

  <div class="footer footer-front">www.plorvaeducationalconsultants.example</div>
  <svg class="footer-arrow" width="36" height="41" viewBox="0 0 36 41"><path d="M0 0h4l32 20.5L4 41H0z" fill="#1b3446"/></svg>
</main>
</body>
</html>
```